Velmora

We need logo and wesbsite for a software development company based out of Hyderabad, India focused on startups and mid sized companies focused on build a new software products in USA and Europe countires.

Target Market(s)

startup and midsized companies in teh USA and Europe for software product development.

Industry/Entity Type

software development

Coding

Coded - Design and coding required

Number of Pages Required

5+ page

Requirements
Must have
• latest design concepts and very elegant
Nice to have
• each page should have images that reflects the content
Should not have
• too many colors

```html
<!DOCTYPE html>
<html lang="en">
<head>
<meta charset="utf-8">
<title>Velmora — Software Development</title>
<link href="https://fonts.googleapis.com/css2?family=Poppins:wght@400;500;600;700&family=Open+Sans:wght@400;600;700&display=swap" rel="stylesheet">
<style>
:root{
  --blue:#1f5fae;
  --blue-deep:#17437f;
  --ink:#22252b;
  --muted:#5d6470;
  --light:#eef0f4;
  --white:#ffffff;
  --footer:#1d2026;
  --footer-bar:#16181d;
}
*{margin:0;padding:0;box-sizing:border-box}
html,body{width:1200px;height:3364px;overflow:hidden}
body{font-family:"Open Sans",sans-serif;color:var(--ink);background:var(--white);position:relative}
h1,h2,h3,.brand,.nav a,.btn{font-family:"Poppins",sans-serif}
section,header,footer{position:absolute;left:0;width:1200px}

/* hero */
.hero{top:0;height:610px;overflow:hidden}
.hero-photo{position:absolute;inset:0;background:linear-gradient(100deg,#1b2530 0%,#2f3b45 35%,#5b6267 60%,#39434a 100%)}
.hero-shade{position:absolute;inset:0;background:linear-gradient(90deg,rgba(10,16,24,.75) 0%,rgba(10,16,24,.35) 55%,rgba(10,16,24,.15) 100%)}
.topbar{position:absolute;top:0;left:0;right:0;height:48px;display:flex;align-items:center;padding:0 110px 0 28px}
.brand{display:flex;align-items:center;gap:8px;color:var(--white);font-size:22px;font-weight:600}
.brand-dot{width:26px;height:26px;border-radius:50%;background:var(--white)}
.nav{margin-left:auto;display:flex;gap:30px;align-items:center}
.nav a{color:var(--white);font-size:12px;font-weight:500;text-decoration:none}
.nav .contact{border:1.5px solid var(--white);border-radius:20px;padding:6px 22px;margin-left:26px;font-weight:600}
.hero-social{position:absolute;left:14px;top:250px;display:flex;flex-direction:column;gap:10px}
.hero-social span{width:18px;height:18px;border-radius:50%;border:1px solid rgba(255,255,255,.8)}
.hero-copy{position:absolute;left:112px;top:226px;width:560px}
.hero-copy h1{color:var(--white);font-size:36px;font-weight:700;line-height:44px;letter-spacing:.5px}
.hero-copy p{color:#9cc4ff;font-size:16px;font-weight:600;line-height:22px;margin-top:10px;width:360px}
.btn{display:inline-block;background:var(--blue);color:var(--white);font-size:11px;font-weight:600;border-radius:20px;padding:10px 24px;letter-spacing:.5px}
.hero-copy .btn{margin-top:24px;background:#2568c4;border-radius:4px}
.dots{position:absolute;left:600px;top:574px;display:flex;gap:6px}
.dots span{width:9px;height:9px;border-radius:50%;background:rgba(255,255,255,.5)}
.dots span:first-child{background:var(--white)}

/* section titles */
.section-title{font-size:40px;font-weight:500;text-align:center;color:var(--ink)}
.section-title strong{font-weight:700}
.lead{font-size:11px;line-height:17px;color:var(--muted);text-align:center;margin:14px auto 0;width:960px}

/* about */
.about{top:610px;height:550px;background:var(--light)}
.about-frame{position:absolute;left:140px;top:92px;width:404px;height:274px;border:6px solid var(--blue)}
.about-photo{position:absolute;left:124px;top:106px;width:404px;height:272px;background:linear-gradient(135deg,#2a3440,#4b5866 55%,#6f7b88)}
.about-copy{position:absolute;left:628px;top:120px;width:460px}
.about-copy h2{font-size:40px;font-weight:500}
.about-copy h2 strong{font-weight:700}
.about-copy p{font-size:11px;line-height:18px;color:var(--muted);margin-top:18px}
.about-copy .btn{margin-top:26px}

/* product */
.product{top:1160px;height:620px;background:var(--white)}
.product .section-title{margin-top:92px}
.cards{position:absolute;top:244px;left:112px;display:flex;gap:18px}
.card{position:relative;width:228px;height:278px;border-radius:4px;overflow:hidden}
.card-photo{position:absolute;inset:0}
.card-label{position:absolute;left:0;right:0;bottom:0;height:52px;background:linear-gradient(0deg,rgba(10,14,20,.9),rgba(10,14,20,0));color:var(--white);font-family:"Poppins",sans-serif;font-size:13px;font-weight:600;padding:26px 14px 0}
.arrow{position:absolute;top:362px}

/* team */
.team{top:1780px;height:600px;background:linear-gradient(120deg,#1a4a8c,#215eae 55%,#1b4f96);color:var(--white)}
.team .section-title{color:var(--white);margin-top:44px}
.team .lead{color:#d7e4f6}
.team-cards{position:absolute;top:212px;left:228px;display:flex;gap:22px}
.team-card{width:236px;height:340px;background:var(--white);border-radius:4px;text-align:center;padding:28px 20px 0;color:var(--ink)}
.team-card svg{display:block;margin:0 auto}
.team-card h3{font-size:13px;font-weight:600;line-height:18px;margin-top:18px;min-height:36px}
.team-card p{font-size:10.5px;line-height:16px;color:var(--muted);margin-top:14px}
.more{display:inline-block;margin-top:18px;font-family:"Poppins",sans-serif;font-size:10.5px;font-weight:600;color:var(--blue)}

/* case study */
.cases{top:2380px;height:708px;background:var(--white)}
.cases .section-title{margin-top:76px}
.case{position:absolute;border-radius:4px;overflow:hidden}
.case .card-label{font-size:13px;font-weight:500;height:60px;padding-top:34px}
.case-a{left:112px;top:160px;width:478px;height:400px}
.case-b{left:608px;top:160px;width:480px;height:192px}
.case-c{left:608px;top:368px;width:480px;height:192px}
.cases .btn{position:absolute;left:536px;top:612px;padding:11px 32px}

/* footer */
.footer{top:3088px;height:276px;background:var(--footer);color:#c9ccd2}
.footer .brand{position:absolute;left:112px;top:28px;font-size:24px}
.f-social{position:absolute;left:112px;top:82px;display:flex;gap:8px}
.f-social span{width:26px;height:26px;border-radius:50%;border:1px solid #9aa0a8}
.f-social span:first-child{background:var(--blue);border-color:var(--blue)}
.f-col{position:absolute;top:36px}
.f-col h4{font-family:"Poppins",sans-serif;font-size:13px;font-weight:600;color:var(--white);letter-spacing:.5px;margin-bottom:10px}
.f-col li{list-style:none;font-size:11px;line-height:19px;display:flex;align-items:center;gap:8px}
.f-col li::before{content:"";width:7px;height:7px;border-radius:50%;border:1px solid #8b919a}
.f-contact li::before{display:none}
.f-contact li{align-items:flex-start;line-height:17px;margin-bottom:6px}
.f-contact svg{flex:none;margin-top:2px}
.f-bar{position:absolute;left:0;right:0;bottom:0;height:44px;background:var(--footer-bar);text-align:center;font-size:10px;line-height:44px;color:#9aa0a8}
</style>
</head>
<body>

<header class="hero">
  <div class="hero-photo" role="img" aria-label="Photo of a software team meeting in a modern office"></div>
  <div class="hero-shade"></div>
  <div class="topbar">
    <div class="brand"><span class="brand-dot"></span>Velmora</div>
    <nav class="nav">
      <a>Home</a><a>About Us</a><a>Build Your Product</a><a>Build Your Team</a><a>Case Study</a>
      <a class="contact">CONTACT</a>
    </nav>
  </div>
  <div class="hero-social"><span></span><span></span><span></span><span></span></div>
  <div class="hero-copy">
    <h1>THE TOP SOFTWARE<br>DEVELOPMENT COMPANY</h1>
    <p>Teams are the essence of every business. They can create wonders if built with perfection.</p>
    <span class="btn">GET STARTED</span>
  </div>
  <div class="dots"><span></span><span></span><span></span><span></span></div>
</header>

<section class="about">
  <div class="about-frame"></div>
  <div class="about-photo" role="img" aria-label="Photo of a developer working at multiple monitors"></div>
  <div class="about-copy">
    <h2>About <strong>Us</strong></h2>
    <p>Teams are the essence of every business. They can create wonders if built with perfection. We are a group of entrepreneurs, technocrats, software architects and delivery heads who have come together to serve startups, product companies and enterprises with their product development.</p>
    <p>We are proven in understanding your product and help design, build, maintain and operate your product. Our people quickly set up a team of experts, business analysts and engineers ready to deliver.</p>
    <span class="btn">LEARN MORE</span>
  </div>
</section>

<section class="product">
  <h2 class="section-title">Build Your <strong>Product</strong></h2>
  <p class="lead">As startups are racing to build software as a product, they face stumbling blocks on building software from scratch. One of the reasons is stiff competition. The competition to get the best resources, robust design, and scalable technology is overwhelming.</p>
  <svg class="arrow" style="left:12px" width="14" height="22" viewBox="0 0 14 22"><path d="M12 2 3 11l9 9" fill="none" stroke="#1f5fae" stroke-width="3"/></svg>
  <svg class="arrow" style="left:1128px" width="14" height="22" viewBox="0 0 14 22"><path d="M2 2l9 9-9 9" fill="none" stroke="#1f5fae" stroke-width="3"/></svg>
  <div class="cards">
    <div class="card"><div class="card-photo" role="img" aria-label="Photo of a project manager leading a meeting" style="background:linear-gradient(160deg,#8a97a6,#4e5b68)"></div><div class="card-label">PROJECT MANAGER</div></div>
    <div class="card"><div class="card-photo" role="img" aria-label="Photo of a team lead at a whiteboard" style="background:linear-gradient(160deg,#b7bcc2,#6d747c)"></div><div class="card-label">TEAM LEAD</div></div>
    <div class="card"><div class="card-photo" role="img" aria-label="Photo of a business analyst reviewing charts" style="background:linear-gradient(160deg,#a8a49c,#5c5a55)"></div><div class="card-label">BUSINESS ANALYST</div></div>
    <div class="card"><div class="card-photo" role="img" aria-label="Photo of developers coding on screens" style="background:linear-gradient(160deg,#3d4b59,#1e2630)"></div><div class="card-label">DEVELOPERS</div></div>
  </div>
</section>

<section class="team">
  <h2 class="section-title">Build Your <strong>Team</strong></h2>
  <p class="lead">Break free from traditional recruiting with us. At Velmora, we help you achieve the right organizational stature with suitable talent who take your business to the next level. We have spent years trying to innovate and improve the process of hiring talented individuals who can help businesses move to the next level. We ensure that the candidates we employ for your organization are highly productive and take you to your goals.</p>
  <div class="team-cards">
    <div class="team-card">
      <svg width="46" height="46" viewBox="0 0 46 46" fill="none" stroke="#1f5fae" stroke-width="2"><rect x="9" y="5" width="28" height="36" rx="2"/><path d="M15 15h16M15 22h16M15 29h10"/></svg>
      <h3>PASS COGNITIVE APTITUDE TEST</h3>
      <p>Accepting job applications from the entire world means every role at Velmora receives thousands of applications.</p>
      <span class="more">READ MORE ›</span>
    </div>
    <div class="team-card">
      <svg width="46" height="46" viewBox="0 0 46 46" fill="none" stroke="#1f5fae" stroke-width="2"><rect x="6" y="8" width="34" height="26" rx="2"/><path d="M12 16h22M12 22h22M16 34l-4 6M30 34l4 6"/></svg>
      <h3>PASS ENGLISH PROFICIENCY TEST</h3>
      <p>Someday technological advancements will make it possible for teams to collaborate without sharing a common language.</p>
      <span class="more">READ MORE ›</span>
    </div>
    <div class="team-card">
      <svg width="46" height="46" viewBox="0 0 46 46" fill="none" stroke="#1f5fae" stroke-width="2"><rect x="6" y="14" width="34" height="24" rx="2"/><path d="M17 14V9h12v5M6 24h34"/></svg>
      <h3>PROVE REAL-WORLD JOB SKILLS</h3>
      <p>Of course, there's much more to being a great worker than intelligence and language skills.</p>
      <span class="more">READ MORE ›</span>
    </div>
  </div>
</section>

<section class="cases">
  <h2 class="section-title">Case <strong>Study</strong></h2>
  <div class="case case-a"><div class="card-photo" role="img" aria-label="Photo of colleagues working together on laptops" style="position:absolute;inset:0;background:linear-gradient(150deg,#c9b8a2,#7a6c5e)"></div><div class="card-label">Make Your Admissions Process More Organized</div></div>
  <div class="case case-b"><div class="card-photo" role="img" aria-label="Photo of a graduate at a campus event" style="position:absolute;inset:0;background:linear-gradient(150deg,#6a7480,#343b44)"></div><div class="card-label">Your Graduate Journey's Guide</div></div>
  <div class="case case-c"><div class="card-photo" role="img" aria-label="Photo of a team planning with cutting-edge tools" style="position:absolute;inset:0;background:linear-gradient(150deg,#3f4852,#1f252c)"></div><div class="card-label">Choose a Program Using These Cutting-Edge Tools</div></div>
  <span class="btn">VIEW MORE</span>
</section>

<footer class="footer">
  <div class="brand"><span class="brand-dot"></span>Velmora</div>
  <div class="f-social"><span></span><span></span><span></span><span></span></div>
  <div class="f-col" style="left:428px">
    <h4>QUICK LINKS</h4>
    <ul><li>Home</li><li>About Us</li><li>Build Your Product</li><li>Build Your Team</li><li>Case Study</li></ul>
  </div>
  <div class="f-col" style="left:668px">
    <h4>RESOURCES</h4>
    <ul><li>FAQ</li><li>Contact</li><li>Privacy Policy</li><li>Terms Of Use</li></ul>
  </div>
  <div class="f-col f-contact" style="left:900px">
    <h4>CONTACT</h4>
    <ul>
      <li><svg width="10" height="12" viewBox="0 0 10 12"><path d="M5 11S1 6.5 1 4a4 4 0 0 1 8 0c0 2.5-4 7-4 7z" fill="none" stroke="#c9ccd2"/><circle cx="5" cy="4" r="1.4" fill="#c9ccd2"/></svg>Plot 12, Madhapur Road,<br>Hyderabad, India</li>
      <li><svg width="10" height="12" viewBox="0 0 10 12"><path d="M2 1h2l1 3-1.5 1a6 6 0 0 0 2.5 3l1-1.5 3 1v2c-5 1-9-4-8-8.5z" fill="#c9ccd2"/></svg>+1 (555) 014 2290</li>
      <li><svg width="11" height="10" viewBox="0 0 11 10"><rect x=".5" y="1.5" width="10" height="7" fill="none" stroke="#c9ccd2"/><path d="M.5 1.5 5.5 6l5-4.5" fill="none" stroke="#c9ccd2"/></svg>info@velmora.com</li>
    </ul>
  </div>
  <div class="f-bar">© 2021 Velmora. All Rights Reserved</div>
</footer>

</body>
</html>
```